Past the Gravel

I need a book cover designed - 6 inches wide x 9 inches tall. I would like it Past the predominantly black and white, with a big bold title as attached:
Past the
GRAVEL
I have attached a black and white photo that I would like to cover the bottom half (or close to it) of the book, with the words: Life Lessons That Helped Build QTR, Pike B Dam, And Transform Loviter & BLUZ TV
By Gavin Melrose
The designs I've included here I don't particularly like, although I think you can see my general idea. He is a black and white man, so I have a back and white photo.
A big bold headline and not overly sized black and white

```html
<!DOCTYPE html>
<html lang="en">
<head>
<meta charset="utf-8">
<title>Past the Gravel — Book Cover</title>
<link href="https://fonts.googleapis.com/css2?family=Crimson+Pro:ital,wght@0,400;0,600;0,700;1,400&family=Vollkorn:wght@700;800&display=swap" rel="stylesheet">
<style>
  :root {
    --page: #ffffff;
    --cover: #0b0b0b;
    --glow: #5b6264;
    --ink-light: #ffffff;
    --ink-dark: #000000;
    --photo-hi: #5a5d5e;
    --photo-mid: #2a2c2d;
    --photo-lo: #0d0d0d;
  }
  * { margin: 0; padding: 0; box-sizing: border-box; }
  html, body {
    width: 1200px;
    height: 1000px;
    overflow: hidden;
    background: var(--page);
  }
  .book-cover {
    position: absolute;
    left: 314px;
    top: 71px;
    width: 569px;
    height: 857px;
    background: var(--cover);
    overflow: hidden;
    box-shadow: 2px 4px 6px rgba(0,0,0,0.35);
  }
  .title-glow {
    position: absolute;
    left: 20px;
    top: 90px;
    width: 530px;
    height: 260px;
    background: radial-gradient(ellipse at 50% 50%, var(--glow) 0%, rgba(60,66,68,0.6) 30%, rgba(11,11,11,0) 70%);
  }
  .title {
    position: absolute;
    left: 0;
    top: 80px;
    width: 569px;
    height: 260px;
  }
  .title text {
    font-family: "Vollkorn", "Crimson Pro", serif;
    font-weight: 800;
    text-anchor: middle;
  }
  .title .extrude {
    fill: var(--ink-dark);
    stroke: var(--ink-light);
    stroke-width: 2.5;
  }
  .title .face {
    fill: var(--ink-light);
    stroke: var(--ink-dark);
    stroke-width: 3;
    paint-order: stroke;
  }
  .author-photo {
    position: absolute;
    left: 280px;
    top: 360px;
    width: 289px;
    height: 497px;
    background:
      radial-gradient(ellipse 55% 40% at 58% 38%, var(--photo-hi) 0%, var(--photo-mid) 55%, rgba(13,13,13,0) 100%),
      linear-gradient(180deg, rgba(11,11,11,0) 0%, var(--photo-lo) 100%);
  }
  .subtitle {
    position: absolute;
    left: 46px;
    top: 358px;
    font-family: "Crimson Pro", serif;
    font-style: italic;
    font-weight: 400;
    font-size: 19px;
    line-height: 37px;
    color: var(--ink-light);
  }
  .byline {
    position: absolute;
    left: 46px;
    top: 732px;
    font-family: "Crimson Pro", serif;
    font-size: 31px;
    font-weight: 400;
    color: var(--ink-light);
  }
  .byline strong { font-weight: 700; }
</style>
</head>
<body>
  <main class="book-cover">
    <div class="title-glow"></div>
    <svg class="title" viewBox="0 0 569 260" aria-label="Past the GRAVEL">
      <text class="extrude" x="290" y="96" font-size="86">Past the</text>
      <text class="face" x="284.5" y="90" font-size="86">Past the</text>
      <text class="extrude" x="291" y="233" font-size="112">GRAVEL</text>
      <text class="face" x="284.5" y="224" font-size="112">GRAVEL</text>
    </svg>
    <div class="author-photo" role="img" aria-label="Black and white portrait photograph of the author"></div>
    <p class="subtitle">
      Life Lessons That Helped<br>
      Build QTR, Pike B Dam,<br>
      and Transform<br>
      Loviter &amp; BLUZ TV
    </p>
    <p class="byline">By <strong>Gavin Melrose</strong></p>
  </main>
</body>
</html>
```